依頼詳細
デザインを依頼する製品の名前は「雲居そば」です。
表面のデザイン作成をお願いします。

【デザインイメージ】
・シックで高級感のあるデザインが好ましいです。
・希望の色はベースが黒色で商品名の「雲居そば」は金色でお願いします。

【必須記載事項】
下記の文言は必ずデザイン上に記載をお願いします。
・ゆで時間4~5分
・内容量220g
・「謹製」(四角の判子風)
・「本場信州の伝統の味」
・「そばの豊かな香りと喉ごしの良さを楽しめます」

【その他製品特徴】
下記はその他製品の特徴になります。デザインへの記載は各ランサー様へお任せします。
・本品「雲居そば」は、本場信州の恵まれた気候風土と長年の経験の中から独自の製法を編み出し、生まれました。のどごしの良いなめらかな食感と風味豊かな香りを楽しめるそばに仕上げました。
・本品は贈答品で使用することが多いため、化粧箱に入っている状態で見栄えが良く見えるデザインをお願いします。また参考となる画像を添付いたします。
記載項目
製品サイズ(実寸):295×75(mm)
希望イメージ
シンプル 複雑
単色 カラフル
暗い 明るい
日常 高級
遊び心 厳粛
未来的 伝統的
女性的 男性的
希望する色
無彩色系
納品ファイル
• 高解像度JPG (.jpg)
• イラストレーター形式 (.ai)

当社がイメージした通り、シックで高級感があり化粧箱に入っている状態で見栄えが良く見えるデザインで、社内のアンケートでも好評だったため選定させていただきました。

この度は、たくさんのご提案を頂き、大変ありがとうございます。
さまざまなデザイン案やコンセプトがあり、選考に時間をいただいてしまいました。
提案者の皆様の非常にクオリティの高い提案に加え、さまざまな方向性のデザインがありとても良い勉強になりました。

```html
<!DOCTYPE html>
<html lang="ja">
<head>
<meta charset="utf-8">
<title>雲居そば パッケージ表面</title>
<link rel="stylesheet" href="https://fonts.googleapis.com/css2?family=Shippori+Mincho+B1:wght@600;800&display=swap">
<style>
  :root {
    --ink: #0d0d0d;
    --gold: #b59b55;
    --gold-light: #d3bd7c;
    --gold-dark: #8c7538;
    --seal-red: #b3232a;
    --white: #ffffff;
  }
  html, body {
    margin: 0;
    padding: 0;
    width: 1200px;
    height: 3536px;
    overflow: hidden;
    background: var(--ink);
  }
  .package {
    position: relative;
    width: 1200px;
    height: 3536px;
    background: var(--ink);
    overflow: hidden;
    font-family: "Shippori Mincho B1", serif;
  }
  .decor {
    position: absolute;
    inset: 0;
    width: 1200px;
    height: 3536px;
  }
  .vertical {
    position: absolute;
    writing-mode: vertical-rl;
    text-orientation: upright;
    margin: 0;
    white-space: nowrap;
  }
  .origin-frame {
    position: absolute;
    left: 470px;
    top: 380px;
    width: 130px;
    height: 700px;
    border: 5px solid var(--gold);
    box-sizing: border-box;
    outline: 2px solid var(--gold);
    outline-offset: 8px;
    display: flex;
    align-items: center;
    justify-content: center;
  }
  .origin-frame .tagline {
    position: static;
    color: var(--gold-light);
    font-weight: 600;
    font-size: 62px;
    line-height: 1;
    letter-spacing: 6px;
  }
  .product-name {
    left: 615px;
    top: 420px;
    color: var(--gold);
    font-weight: 800;
    font-size: 380px;
    line-height: 1;
    letter-spacing: 10px;
  }
  .description {
    left: 335px;
    top: 470px;
    color: var(--gold);
    font-weight: 600;
    font-size: 62px;
    line-height: 1;
    letter-spacing: 6px;
  }
  .seal {
    position: absolute;
    left: 318px;
    top: 2050px;
    width: 110px;
    height: 230px;
    border: 7px solid var(--seal-red);
    border-radius: 10px;
    box-sizing: border-box;
    display: flex;
    align-items: center;
    justify-content: center;
  }
  .seal span {
    writing-mode: vertical-rl;
    text-orientation: upright;
    color: var(--seal-red);
    font-weight: 800;
    font-size: 86px;
    line-height: 1;
  }
  .boil-time {
    position: absolute;
    left: 420px;
    top: 3180px;
    width: 360px;
    height: 200px;
    background: var(--ink);
    border: 5px solid var(--white);
    border-radius: 22px;
    box-sizing: border-box;
    color: var(--white);
    text-align: center;
    font-weight: 600;
    font-size: 64px;
    line-height: 1.2;
    padding-top: 18px;
  }
  .net-weight {
    position: absolute;
    left: 0;
    width: 1200px;
    top: 3405px;
    text-align: center;
    color: var(--ink);
    font-weight: 800;
    font-size: 64px;
    line-height: 1;
    margin: 0;
  }
</style>
</head>
<body>
<main class="package">
  <svg class="decor" viewBox="0 0 1200 3536">
    <defs>
      <linearGradient id="paperTone" x1="0" y1="0" x2="1" y2="1">
        <stop offset="0" stop-color="#cfcfcf"/>
        <stop offset="0.5" stop-color="#8f8f8f"/>
        <stop offset="1" stop-color="#dcdcdc"/>
      </linearGradient>
    </defs>

    <g role="img" aria-label="金色の和柄リボン">
      <polygon points="60,110 1160,60 1160,120 60,170" fill="#b59b55"/>
      <polygon points="300,170 1120,140 1120,200 300,230" fill="#d3bd7c"/>
      <polygon points="0,100 80,95 80,150 0,155" fill="#8c7538"/>
    </g>

    <g fill="#b59b55">
      <rect x="150" y="40" width="40" height="40" transform="rotate(20 170 60)"/>
      <rect x="560" y="20" width="36" height="36" transform="rotate(35 578 38)"/>
      <rect x="1060" y="240" width="44" height="44" transform="rotate(15 1082 262)"/>
      <rect x="1000" y="1700" width="34" height="34" transform="rotate(30 1017 1717)"/>
      <rect x="860" y="1600" width="28" height="28" transform="rotate(45 874 1614)"/>
      <rect x="1100" y="1500" width="30" height="30" transform="rotate(10 1115 1515)"/>
      <rect x="700" y="1820" width="26" height="26" transform="rotate(25 713 1833)"/>
      <rect x="960" y="1400" width="22" height="22" transform="rotate(40 971 1411)"/>
    </g>

    <polygon role="img" aria-label="和紙の質感" fill="url(#paperTone)"
      points="0,2200 260,2120 520,2000 760,1880 980,1760 1200,1680 1200,3536 0,3536"/>

    <g fill="#0d0d0d">
      <rect x="820" y="2000" width="50" height="50" transform="rotate(30 845 2025)"/>
      <rect x="540" y="2300" width="40" height="40" transform="rotate(15 560 2320)"/>
      <rect x="980" y="2560" width="44" height="44" transform="rotate(40 1002 2582)"/>
      <rect x="380" y="2620" width="36" height="36" transform="rotate(20 398 2638)"/>
      <rect x="660" y="2900" width="48" height="48" transform="rotate(35 684 2924)"/>
    </g>

    <g role="img" aria-label="金色の青海波柄の帯">
      <rect x="0" y="2300" width="900" height="70" fill="#d3bd7c"/>
      <rect x="250" y="2420" width="950" height="80" fill="#b59b55"/>
      <rect x="0" y="2560" width="780" height="70" fill="#c9b06a"/>
      <rect x="400" y="2690" width="800" height="80" fill="#d3bd7c"/>
      <rect x="0" y="2830" width="1000" height="70" fill="#a58c4a"/>
      <rect x="650" y="2960" width="550" height="70" fill="#d3bd7c"/>
      <rect x="0" y="3390" width="1200" height="146" fill="#c9b06a"/>
    </g>

    <g fill="#0d0d0d">
      <rect x="500" y="3120" width="200" height="60" rx="8"/>
      <rect x="480" y="3100" width="240" height="22" rx="6"/>
      <rect x="580" y="3078" width="40" height="24" rx="6"/>
      <rect x="440" y="3130" width="60" height="18" rx="6"/>
      <rect x="700" y="3130" width="60" height="18" rx="6"/>
    </g>
  </svg>

  <div class="origin-frame">
    <p class="vertical tagline">本場信州の伝統の味</p>
  </div>

  <h1 class="vertical product-name">雲居そば</h1>

  <p class="vertical description">そばの豊かな香りと喉ごしの良さを楽しめます</p>

  <div class="seal"><span>謹製</span></div>

  <div class="boil-time">ゆで時間<br>4〜5分</div>

  <p class="net-weight">内容量220g</p>
</main>
</body>
</html>
```